Email signature design - law firm

We are a small boutique law firm which is located near the beach in Manly, Australia.

We have just recently developed a new logo and are looking to redesign our letterhead, business cards and email signatures.

This brief is for our email signatures. This is an email signature to appear at the bottom of our Outlook emails so we would like it to be text that we are able to edit as the wording in our email signature often required amendments.

I have attached a word document which had our new logo, and our previous email signature which all the information/wording that needs to be included.

We would like multiple designs with a modern, simplistic yet striking look.

Thanks.

font - raleway or montserrat

Need extra days to review

• Must have the exact wording which appears in the email signature in the word document attached to brief.
• Must be able to edit the text as it is for an Outlook email signature which wording will change from time to time.

```html
<!DOCTYPE html>
<html lang="en">
<head>
<meta charset="utf-8">
<title>Email Signature – Harbourne &amp; Partners Lawyers</title>
<link rel="stylesheet" href="https://fonts.googleapis.com/css2?family=Carlito:wght@400;700&display=swap">
<style>
  :root {
    --ink: #111111;
    --navy: #2b3a8c;
    --gold: #c9a227;
    --divider: #1a1a1a;
    --page: #ffffff;
  }
  * { box-sizing: border-box; margin: 0; padding: 0; }
  html, body {
    width: 1200px;
    height: 1000px;
    overflow: hidden;
    background: var(--page);
  }
  body {
    font-family: "Carlito", sans-serif;
    color: var(--ink);
  }
  .signature {
    position: absolute;
    left: 40px;
    top: 150px;
    width: 1120px;
  }
  .sign-off { font-size: 14px; margin-bottom: 18px; }
  .sender-name { font-size: 14px; font-weight: 700; margin-bottom: 22px; }
  .firm-mark {
    display: flex;
    align-items: center;
    gap: 10px;
    height: 100px;
    margin-left: 8px;
    margin-bottom: 18px;
  }
  .firm-mark .dot {
    width: 14px; height: 14px;
    border-radius: 50%;
    background: var(--navy);
  }
  .firm-name {
    font-size: 17px;
    font-weight: 700;
    color: var(--navy);
    line-height: 1.3;
    letter-spacing: 0.5px;
  }
  .contact { font-size: 14px; line-height: 19px; }
  .contact .sep { color: var(--navy); padding: 0 3px; }
  .contact .label { color: var(--gold); }
  .divider {
    border: none;
    border-top: 2px solid var(--divider);
    margin: 18px 0 20px;
  }
  .legal {
    width: 620px;
    font-size: 10.5px;
    line-height: 15.6px;
  }
  .legal p + p { margin-top: 15px; }
</style>
</head>
<body>
  <main class="signature">
    <p class="sign-off">Regards</p>
    <p class="sender-name">Nadia Fenwick</p>

    <div class="firm-mark">
      <span class="dot"></span>
      <span class="firm-name">Harbourne &amp; Partners<br>Lawyers</span>
    </div>

    <div class="contact">
      <p>Suite 4<span class="sep">|</span>12 Corso Lane<span class="sep">|</span>SEAVIEW NSW 2099</p>
      <p><span class="label">T:</span> (02) 9000 4118<span class="sep">|</span><span class="label">F:</span> (02) 9000 4119</p>
    </div>

    <hr class="divider">

    <section class="legal">
      <p>Important note: This E-Mail and any attachment is PRIVILEGED and confidential.&nbsp; It must not be read, copied, disclosed or used by any person other than the above named addressees.&nbsp; In order to preserve the intended confidentiality and privilege, please notify us immediately if you have received this e-mail by mistake and secure-delete this e-mail from your system. Unauthorised perusal, use, disclosure, forwarding or copying is strictly prohibited and may be unlawful.</p>
      <p>Liability limited by a scheme approved under Professional Standards Legislation. Legal practitioners at SeaviewLegal (NSW) Pty Ltd are members of the scheme.</p>
      <p>Fraud warning: Please be aware that there is a significant risk posed by cyber fraud, specifically relating to email accounts and bank account details. Our bank account details will never change during the course of a transaction, and we will never advise you of a change to our bank details via email.&nbsp; Please check account details with us in person or by phone before making payments.&nbsp; If you advise us of your bank account details by email, please also ring and confirm the bank account details by phone as well.</p>
    </section>
  </main>
</body>
</html>
```